Website Redesign Project

Bright Harbour Consulting provides project management and project controls consultancy services to companies in many industry sectors, within Australia and overseas. My company has been developing a business brand through forging strong business relationships within industry. We provide innovative tools, concepts and solutions to management teams to assist them in better plan and managing there project portfolios.
SECTORS OF INDUSTRY WE SERVICE
★Oil & Gas
★Minerals & Metals
★Petrochemical
★Manufacturing
★Building & Construction
★Telecommunications
★Rail
★Civil
OLD WEBSITE
My old website www.brightharbourconsulting.com.au needs a complete overhaul in terms of how the web pages look and feel. I am trying to get away from the grey, washed out look as it is uninviting and dull. My clients commented that my webpage does not reflect who I am as a company or my core values. Think total redesign
DESIGN
I would like a webpage design that is modern and has a corporate image. It must be elegant, classy, and have an overall glossy appearance. I want something exciting that creates some excellent feedback from clients. It needs to have a savvy appearance and an attitude of a market leader. A generic website template cannot be used as I provide a unique service to clients. I do not need a website design that looks like my compeditors, I want something that stands out in the crowd and effectivly markets my bussinesses brand. I want my website to represent quality, so only high resolution images that are clear, sharp and in focus can be used. With this design, throw your standard webpage design concepts out the window, as I want something fresh, innovative, exciting and inviting. The overall design should appear uncluttered as all content needs to be there for a reason, so think functional.
It must be professional and of the highest calibre as my clients expect nothing less. I provide clients with innovative tools, concepts and solutions, so the design needs to be edgy and creative to align with my company’s core business services. The new design must promote the company’s brand and us as a market leader. It must communicate that we service many industry sectors and reflect our company’s creativity, vision, energy and drive.
WEBPAGE WRITTEN CONTENT
I am happy with the written content on each page within my old website. You may arrange the text how you see fit within the new design. On the main page of my old website the text is under scored, I am not a big fan of this. I currently do not like the format the text is in, I am looking for a formatt that is easy to read, looks flattering and pleasing to the eye.
MAIN PAGE DESIGN
The main page design needs to focus on my company as a brand, it must promote that I service many industry sectors. My old webpage had me pigeon holed as only providing services to oil and gas. This is incorrect as I service oil & gas, metals and minerals, Petrochemical, Manufacturing, Building & Construction, Telecommunications, Rail and civil.
WEBPAGE COLUR PREFERENCE
Prefer a white background with plenty of colour
TESTIMONIAL TAB
The testimonial tab on the task bar can be removed as it is no longer required.
FINISHED PRODUCT
The finished product will be uploaded by you to a nominated web hosting account. I will need a copy of all files associated with the design. A copy of the finished product will also be provided in formats that can me imported to Xara Pro Designer as I will update my website in 6 months or so using this tool.
Updates
I have updated the design brief after recieving feedback from several designers
Thanks
Hi All
I have just launched another project called "bright harbour consulting business card redesign project", you are all welcome to join this project.
Thanks
Target Market(s)
★Oil and Gas
★Mining and Resources
★Building and infrastructure
★Petrochemical
★Civil and roads
★Rail
Industry/Entity Type
Industry
Requirements
Must have
- ★Draw you in
★Hold your attention
★Identify company brand
★Highlight skills experience and expertise
★Be a unique design not generic
Should not have
- ★The webpage design should not be old fashioned
★ The design should not be based off a generic design template
★The webpage should not be cluttered; everything needs to be there for a reason.

```html
<!DOCTYPE html>
<html lang="en">
<head>
<meta charset="utf-8">
<title>Bright Harbour Consulting</title>
<link rel="stylesheet" href="https://fonts.googleapis.com/css2?family=Signika:wght@400;600&family=Arimo:wght@400;700&family=Source+Sans+3:wght@400;600&display=swap">
<style>
:root{
  --ink:#111;
  --nav:#8a8a8a;
  --foot-head:#555;
  --foot-text:#9a9a9a;
  --tile-dark:#5e5e5e;
  --tile-grey:#9a9a9c;
  --tile-red:#f2392f;
  --tile-blue:#4aa3df;
  --brand-red:#e1252a;
  --white:#fff;
}
*{margin:0;padding:0;box-sizing:border-box}
html,body{width:1185px;height:1200px;overflow:hidden;background:var(--white)}
body{position:relative;font-family:"Arimo",Arial,sans-serif;color:var(--ink)}

.brand{position:absolute;left:134px;top:30px;display:flex;align-items:center;gap:10px}
.brand-mark{width:44px;height:44px;border-radius:50%;background:var(--brand-red);flex:none}
.brand-name{font-family:"Signika",sans-serif;font-weight:600;font-size:26px;color:var(--ink);letter-spacing:-.3px;line-height:1}
.brand-tag{font-family:"Arimo",sans-serif;font-size:8px;color:#333;margin-top:4px}

.hotline{position:absolute;left:864px;top:36px;display:flex;align-items:center;gap:9px}
.hotline svg{width:34px;height:34px}
.hotline-label{font-family:"Source Sans 3",sans-serif;font-size:13px;color:#555;margin-left:8px}
.hotline-number{font-family:"Source Sans 3",sans-serif;font-size:17px;color:var(--ink);line-height:1}

.main-nav{position:absolute;top:109px;left:0;width:1185px;height:20px}
.main-nav a{position:absolute;font-family:"Source Sans 3",sans-serif;font-size:13.5px;color:var(--nav);text-decoration:none}

.tile{position:absolute;border-radius:4px;overflow:hidden}
.tile-text{color:var(--white);padding:22px 15px 0 15px}
.tile h2{font-family:"Signika",sans-serif;font-weight:600;font-size:26px;line-height:29px;letter-spacing:.3px;margin-left:-1px;margin-bottom:13px}
.tile p{font-size:11.3px;line-height:16.7px;text-align:justify}
.more{position:absolute;left:16px;bottom:18px;font-weight:700;font-size:12px;color:var(--white);text-decoration:none}
.tile-icon{position:absolute;right:12px;bottom:10px;opacity:.35}

.expertise{left:148px;top:141px;width:288px;height:288px;background:var(--tile-dark)}
.experience{left:148px;top:442px;width:288px;height:288px;background:var(--tile-grey)}
.pm{left:749px;top:442px;width:288px;height:288px;background:var(--tile-red)}
.client{left:448px;top:743px;width:288px;height:288px;background:var(--tile-blue)}
.pm .tile-icon{opacity:.9}

.photo{position:absolute;border-radius:4px}
.photo-refinery{left:451px;top:142px;width:583px;height:286px;background:linear-gradient(180deg,#3a3f86 0%,#7a6aa8 45%,#b98a8a 62%,#3a3340 78%,#121218 100%)}
.photo-refinery p{position:absolute;left:19px;right:28px;bottom:11px;color:var(--white);font-size:12.6px;line-height:16.7px}
.photo-refinery .arrow{position:absolute;right:15px;bottom:12px;color:var(--brand-red);font-size:11px;font-weight:700}
.photo-helmet{left:447px;top:442px;width:290px;height:288px;background:linear-gradient(135deg,#eef1f4 0%,#dfe4e8 35%,#e83a2a 60%,#b71d14 85%,#dde2e6 100%)}
.photo-welding{left:147px;top:743px;width:290px;height:288px;background:radial-gradient(circle at 45% 55%,#bfe6ff 0%,#3d8fd0 25%,#1c3d6a 55%,#0d1422 100%)}
.photo-chart{left:749px;top:743px;width:288px;height:288px;background:linear-gradient(160deg,#f2f5f9 0%,#d5dde8 55%,#485a78 100%)}

.footer-col{position:absolute;top:1056px}
.footer-col h3{font-family:"Arimo",sans-serif;font-weight:400;font-size:12px;color:var(--foot-head);margin-bottom:13px}
.footer-col ul{list-style:none;margin-left:1px}
.footer-col li{font-size:10px;line-height:16.7px;color:var(--foot-text)}
.col-who{left:149px}
.col-what{left:337px}
.col-contact{left:525px}
.col-contact ul{margin-left:4px}

.footer-brand{position:absolute;right:152px;top:1055px;display:flex;align-items:center;gap:6px}
.footer-brand .brand-mark{width:22px;height:22px}
.footer-brand .brand-name{font-size:14px}
.copyright{position:absolute;right:152px;top:1099px;font-size:10px;color:var(--foot-text)}
.social{position:absolute;right:146px;top:1136px;display:flex;gap:9px}
.social span{width:23px;height:23px;border-radius:50%;background:#b5b5b5}
</style>
</head>
<body>

<header>
  <div class="brand">
    <span class="brand-mark"></span>
    <div>
      <div class="brand-name">Bright Harbour Consulting</div>
      <div class="brand-tag">Providing Effective Project Controls and Management Solutions</div>
    </div>
  </div>

  <div class="hotline">
    <svg viewBox="0 0 34 34" aria-hidden="true">
      <circle cx="17" cy="17" r="15.5" fill="none" stroke="#222" stroke-width="1.6"/>
      <path d="M12 9c-2 1-2 4-1 7 1.5 4 4 7 7 9 2 1 4 1 5-1l-2.5-2.5-2 1.5c-2-1-4-4-5-6l1.5-2z" fill="#222"/>
    </svg>
    <div>
      <div class="hotline-label">CALL 27/7</div>
      <div class="hotline-number">+ 61 0400 555 019</div>
    </div>
  </div>

  <nav class="main-nav">
    <a href="#" style="left:455px">ABOUT US</a>
    <a href="#" style="left:552px">EXPERTISE</a>
    <a href="#" style="left:655px">KNOWLEDGE</a>
    <a href="#" style="left:776px">EXPERIENCE</a>
    <a href="#" style="left:888px">PROJECTS</a>
    <a href="#" style="left:995px">FOCUS</a>
  </nav>
</header>

<main>
  <section class="tile expertise">
    <div class="tile-text">
      <h2>EXPERTISE</h2>
      <p>Equipped and licenced to use the latest Keystone PX Enterprise Project Portfolio Management software..</p>
    </div>
    <a class="more" href="#">MORE »</a>
    <svg class="tile-icon" width="58" height="50" viewBox="0 0 58 50" aria-hidden="true">
      <path d="M3 2v45h53" fill="none" stroke="#222" stroke-width="4"/>
      <path d="M12 34l12-10 10 8 16-20" fill="none" stroke="#222" stroke-width="4"/>
      <circle cx="50" cy="12" r="5" fill="#222"/>
    </svg>
  </section>

  <div class="photo photo-refinery" role="img" aria-label="Oil refinery lit up at dusk">
    <p>I provide services to companies in the mining and oil and gas sector to enabling them to plan and manage their construction projects more effectively. This is achieved by evaluating the businesses practices and them implementing different tools and solutions..</p>
    <span class="arrow">&gt;&gt;</span>
  </div>

  <section class="tile experience">
    <div class="tile-text">
      <h2>EXPERIENCE</h2>
      <p>While at Northwind Energy I implemented two project initiatives, the first was designing and implementing an accommodation management tool to assist admin with bookings, the second was to develop a Ledgerline Base database to manage project labour and expenditure.</p>
    </div>
    <a class="more" href="#">MORE »</a>
    <svg class="tile-icon" width="60" height="60" viewBox="0 0 60 60" aria-hidden="true">
      <g fill="none" stroke="#333" stroke-width="3">
        <circle cx="14" cy="52" r="5"/><circle cx="30" cy="52" r="5"/>
        <path d="M14 46c0-14 10-24 24-30M30 46c4-12 14-18 22-20"/>
        <path d="M4 20l8 8M12 20l-8 8M20 28l8 8M28 28l-8 8"/>
      </g>
    </svg>
  </section>

  <div class="photo photo-helmet" role="img" aria-label="Red hard hat resting on construction plans"></div>

  <section class="tile pm">
    <div class="tile-text">
      <h2>PROJECT<br>MANAGEMENT</h2>
      <p>I have assisted clients to achieve this on medium to large scale projects within Australia and Overseas. Preconfigured project templates can be customised to suit your projects requirements.</p>
    </div>
    <a class="more" href="#">MORE »</a>
    <svg class="tile-icon" width="64" height="58" viewBox="0 0 64 58" aria-hidden="true">
      <rect x="2" y="30" width="44" height="26" fill="none" stroke="#d01d16" stroke-width="5"/>
      <rect x="20" y="2" width="40" height="40" fill="none" stroke="#d01d16" stroke-width="5"/>
    </svg>
  </section>

  <div class="photo photo-welding" role="img" aria-label="Welder cutting a steel pipe with sparks flying"></div>

  <section class="tile client">
    <div class="tile-text">
      <h2>CLIENT<br>ENGAGEMENT</h2>
      <p>Work can be conducted at the client's premises or externally. This normally depends on the type of work being discussed and how much interfacing is required with other team members</p>
    </div>
    <a class="more" href="#">MORE »</a>
    <svg class="tile-icon" width="60" height="60" viewBox="0 0 60 60" aria-hidden="true" style="opacity:.45">
      <path d="M28 8a26 26 0 1 0 26 26H28z" fill="#1f6fb0"/>
      <path d="M33 2a25 25 0 0 1 25 25H33z" fill="#1f6fb0"/>
    </svg>
  </section>

  <div class="photo photo-chart" role="img" aria-label="Pen resting on a printed financial bar chart"></div>
</main>

<footer>
  <div class="footer-col col-who">
    <h3>WHO WE ARE</h3>
    <ul><li>Home</li><li>About Us</li><li>Contact Us</li><li>Focous</li><li>Knowledge</li></ul>
  </div>
  <div class="footer-col col-what">
    <h3>WHAT WE DO</h3>
    <ul><li>Experience</li><li>Expertise</li><li>Customer Relations</li><li>Projects</li><li>Requietment</li></ul>
  </div>
  <div class="footer-col col-contact">
    <h3>CONTACT US</h3>
    <ul><li>Liam Carter</li><li>Tel: 0400555019</li><li>Email: liamcarter@bhc.com.au</li></ul>
  </div>

  <div class="footer-brand">
    <span class="brand-mark"></span>
    <span class="brand-name">Bright Harbour Consulting</span>
  </div>
  <div class="copyright">Brightharbourconsulting. All Rights Reserved ©Copyright by 2013</div>
  <div class="social" aria-label="Social links"><span></span><span></span><span></span></div>
</footer>

</body>
</html>
```